Ardenwell Building and Property Services needs a business card design

We need a business card design for our building and property services business. We already have a logo we just need a creative design and layout on a business card. Emphasis on clean, modern, professional.
Our client targets are mainly body corporates, building managers, construction managers.
We are a building services company that lean more to structural repair of buildings, through concrete rectification and carbon fibre strengthening.
We also refurbish facades, rendering, painting etc
We target higher end body corporates in prestigious locations, hence why we'd like our cards to reflect professionalism, strength, efficiency

Target Market(s)

body corporates, building managers, construction managers

Industry/Entity Type

Construction

Contact Information for Business Card

Ardenwell is the main word, with 'Building and Property Services' underneath.
Level 17, 82 Harlow Street
MERRIDALE
Melbourne
Vic 3094
T: 9518 2736
Duncan Ferris - Director
dunardenwell@mailbox-example.com

Requirements
Must have
• Stand out on the back of the card- strong/ bold, company logo
• All of the contact details written above
Should not have
• I'd like the card to stand out, especially on the back. Id like the company logo to be prominent, although feel free to be creative around it. But remain clean and professional

```html
<!DOCTYPE html>
<html lang="en">
<head>
<meta charset="utf-8">
<title>Ardenwell Building and Property Services – Business Card</title>
<link rel="stylesheet" href="https://fonts.googleapis.com/css2?family=Quicksand:wght@300;500&family=Noticia+Text&display=swap">
<style>
  :root {
    --backdrop: #3b3b3b;
    --card-front: #a4a4a4;
    --card-back: #fbfbfc;
    --band: #050505;
    --band-text: #ffffff;
    --ink: #111111;
    --brand-blue: #1f78c8;
    --brand-blue-deep: #1560a8;
    --contact-blue: #3a8fd0;
    --shadow: rgba(0, 0, 0, 0.45);
  }
  * { margin: 0; padding: 0; box-sizing: border-box; }
  html, body {
    width: 1200px;
    height: 840px;
    overflow: hidden;
    background: var(--backdrop);
  }
  .canvas {
    position: relative;
    width: 1200px;
    height: 840px;
  }
  .card {
    position: absolute;
    width: 551px;
    height: 353px;
    overflow: hidden;
    box-shadow: 0 6px 18px var(--shadow);
  }
  .card--front { left: 60px; top: 50px; background: var(--card-front); }
  .card--back  { left: 590px; top: 440px; background: var(--card-back); }

  .band {
    position: absolute;
    background: var(--band);
  }
  .band--upper-left  { left: 0; width: 360px; height: 38px; }
  .band--upper-right { right: 0; width: 92px; height: 38px; }
  .band--lower       { left: 0; width: 100%; height: 38px; }
  .card--front .band--upper-left,
  .card--front .band--upper-right { top: 127px; }
  .card--front .band--lower { top: 176px; }
  .card--back .band--upper-left,
  .card--back .band--upper-right { top: 130px; }
  .card--back .band--lower { top: 178px; }

  .company-name {
    position: absolute;
    left: 27px;
    top: 66px;
    font-family: "Quicksand", sans-serif;
    font-weight: 300;
    font-size: 52px;
    line-height: 1;
    color: var(--ink);
  }
  .company-tagline {
    position: absolute;
    left: 36px;
    top: 127px;
    height: 38px;
    line-height: 38px;
    font-family: "Noticia Text", serif;
    font-size: 17px;
    color: var(--band-text);
  }

  .brand-mark {
    position: absolute;
    display: flex;
    flex-direction: column;
    align-items: center;
    width: 180px;
  }
  .card--front .brand-mark { left: 315px; top: 122px; }
  .card--back  .brand-mark { left: 323px; top: 124px; }
  .brand-mark__dot {
    width: 96px;
    height: 96px;
    border-radius: 50%;
    background: var(--brand-blue);
  }
  .brand-mark__name {
    margin-top: 8px;
    font-family: "Quicksand", sans-serif;
    font-weight: 500;
    font-size: 22px;
    line-height: 1;
    color: var(--brand-blue-deep);
  }

  .person-name {
    position: absolute;
    left: 14px;
    top: 82px;
    font-family: "Noticia Text", serif;
    font-size: 38px;
    line-height: 1;
    color: var(--ink);
  }
  .person-role {
    position: absolute;
    left: 105px;
    top: 130px;
    height: 38px;
    line-height: 38px;
    font-family: "Noticia Text", serif;
    font-size: 19px;
    color: var(--band-text);
  }

  .contact {
    position: absolute;
    left: 14px;
    font-family: "Noticia Text", serif;
    font-size: 15px;
    line-height: 17.5px;
    color: var(--contact-blue);
    font-style: normal;
  }
  .contact--address { top: 221px; }
  .contact--lines { top: 300px; line-height: 20px; }
  .contact__label {
    display: inline-block;
    width: 28px;
  }
</style>
</head>
<body>
  <main class="canvas">

    <section class="card card--front" aria-label="Card front">
      <div class="band band--upper-left"></div>
      <div class="band band--upper-right"></div>
      <div class="band band--lower"></div>
      <h1 class="company-name">Ardenwell</h1>
      <p class="company-tagline">Building and Property Services</p>
      <div class="brand-mark">
        <span class="brand-mark__dot"></span>
        <span class="brand-mark__name">Ardenwell</span>
      </div>
    </section>

    <section class="card card--back" aria-label="Card back">
      <div class="band band--upper-left"></div>
      <div class="band band--upper-right"></div>
      <div class="band band--lower"></div>
      <h2 class="person-name">Duncan Ferris</h2>
      <p class="person-role">Director</p>
      <div class="brand-mark">
        <span class="brand-mark__dot"></span>
        <span class="brand-mark__name">Ardenwell</span>
      </div>
      <address class="contact contact--address">
        Level 17, 82 Harlow Street<br>
        MERRIDALE<br>
        Melbourne<br>
        Vic 3094
      </address>
      <p class="contact contact--lines">
        <span class="contact__label">T :</span>9518 2736<br>
        <span class="contact__label">E :</span>dunardenwell@mailbox-example.com
      </p>
    </section>

  </main>
</body>
</html>
```